Business Card Design Project - bel soravin group

dear Sirs

we need business card design for our group ( BEL Soravin Group ) , i have got the Logo design of our group from pixel harbor in previous , so all need details relating to our group i think available with you, as well as the the chosen logo design

we hope to provide us with business card logo that to be appropaite and satisfactory to us .

thanks

note : logo design of our group is attached .
Updates

Reason: please extend the deadline of my project for additional 15 days because i didn't received appropriate design for our gruop yet . kindly beaware that i have received 77 design till now , supossed to send me 200-250 design at least . thanks

Target Market(s)

contents
-

name : Korvan EL Mistrani

position : Operation Manager

Industry/Entity Type

Business

Requirements
Must have

• person name

group logo
Nice to have
• logo color matching with back background

```html
<!DOCTYPE html>
<html lang="en">
<head>
<meta charset="utf-8">
<title>BEL Soravin Group – Business Card</title>
<link href="https://fonts.googleapis.com/css2?family=PT+Sans:wght@400;700&display=swap" rel="stylesheet">
<style>
  :root {
    --stage: #e8e5e0;
    --navy-light: #283f86;
    --navy-dark: #15195a;
    --navy-text: #1d2a6b;
    --band-blue: #1b4a8a;
    --accent-blue: #2e6fc0;
    --gold: #dcb452;
    --white: #ffffff;
    --silver: #e4e7ef;
  }
  * { margin: 0; padding: 0; box-sizing: border-box; }
  html, body { width: 1200px; height: 900px; overflow: hidden; }
  body {
    background: var(--stage);
    font-family: "PT Sans", Arial, sans-serif;
    position: relative;
  }
  .card {
    position: absolute;
    left: 312px;
    width: 575px;
    height: 326px;
    border-radius: 10px;
    overflow: hidden;
    box-shadow: 0 6px 18px rgba(0,0,0,0.18);
  }
  /* Front */
  .card-front {
    top: 102px;
    background: linear-gradient(135deg, var(--navy-light) 0%, var(--navy-dark) 100%);
  }
  .front-name {
    position: absolute;
    top: 130px;
    left: 0; right: 0;
    text-align: center;
    color: var(--silver);
    font-weight: 700;
    font-size: 40px;
    line-height: 1.2;
  }
  .front-web {
    position: absolute;
    bottom: 27px;
    left: 0; right: 0;
    text-align: center;
    color: var(--white);
    font-weight: 700;
    font-size: 16px;
  }
  /* Back */
  .card-back {
    top: 442px;
    background: var(--white);
  }
  .contact-band {
    position: absolute;
    left: 0; right: 0; bottom: 0;
    height: 102px;
    background: var(--band-blue);
    border-top: 4px solid var(--gold);
  }
  .person { position: absolute; left: 22px; top: 18px; }
  .person-name { color: var(--navy-text); font-weight: 700; font-size: 21px; line-height: 1.1; }
  .person-role { color: var(--accent-blue); font-weight: 700; font-size: 12px; }
  .back-name {
    position: absolute;
    right: 22px;
    top: 32px;
    color: var(--navy-text);
    font-weight: 700;
    font-size: 30px;
    line-height: 1.2;
  }
  .contact {
    position: absolute;
    color: var(--white);
    font-weight: 700;
    font-size: 12.5px;
    line-height: 1.35;
    display: flex;
    align-items: center;
    gap: 7px;
    white-space: nowrap;
  }
  .contact svg { width: 15px; height: 15px; flex: none; }
  .divider {
    position: absolute;
    top: 264px;
    width: 2px;
    height: 36px;
    background: var(--gold);
  }
</style>
</head>
<body>

<section class="card card-front">
  <div class="front-name">BEL Soravin Group</div>
  <div class="front-web">www.belsoravin.com</div>
</section>

<section class="card card-back">
  <div class="contact-band"></div>

  <div class="person">
    <div class="person-name">Korvan EL Mistrani</div>
    <div class="person-role">Operation Manager</div>
  </div>
  <div class="back-name">BEL Soravin Group</div>

  <div class="contact" style="left:20px; top:250px;">
    <span>1234 Somecity, Some Avenue,<br>Some State, Some Country</span>
  </div>
  <div class="contact" style="left:20px; top:292px;">
    <svg viewBox="0 0 16 16"><circle cx="8" cy="8" r="7" fill="var(--gold)"/><path d="M1 8h14M8 1c-3 4-3 10 0 14M8 1c3 4 3 10 0 14" stroke="var(--band-blue)" stroke-width="1" fill="none"/></svg>
    <span>www.belsoravin.com</span>
  </div>

  <div class="divider" style="left:208px;"></div>

  <div class="contact" style="left:230px; top:264px;">
    <svg viewBox="0 0 16 16"><rect x="3" y="6" width="10" height="8" rx="1" fill="var(--gold)"/><path d="M1 6 Q8 0 15 6 L13 7 Q8 3 3 7 Z" fill="var(--gold)"/></svg>
    <span>1234-567-89-89</span>
  </div>
  <div class="contact" style="left:230px; top:292px;">
    <svg viewBox="0 0 16 16"><rect x="2" y="5" width="12" height="9" rx="1" fill="var(--gold)"/><rect x="5" y="2" width="6" height="4" fill="var(--gold)"/><rect x="4" y="8" width="8" height="1.5" fill="var(--band-blue)"/></svg>
    <span>1234-567-89-89</span>
  </div>

  <div class="divider" style="left:370px;"></div>

  <div class="contact" style="left:392px; top:264px;">
    <svg viewBox="0 0 16 16"><rect x="4" y="1" width="8" height="14" rx="1.5" fill="var(--gold)"/><rect x="5.5" y="3" width="5" height="8" fill="var(--band-blue)"/></svg>
    <span>1234-567-89-89</span>
  </div>
  <div class="contact" style="left:392px; top:292px;">
    <svg viewBox="0 0 16 16"><rect x="1" y="4" width="14" height="9" fill="var(--gold)"/><path d="M1 4 L8 9 L15 4" stroke="var(--band-blue)" stroke-width="1.2" fill="none"/></svg>
    <span>korvan@belsoravin.com</span>
  </div>
</section>

</body>
</html>
```